Tallow Recovery Large Loss Booklet

It will be a booklet brochure, 5 pages of front and back material and covers on both sides. Use the presentation files you already created to make it happen.
Updates

I realized the presentation files by which we were asking everyone to use were not updated. They are now posted with a little more detail. Thank you!

Target Market(s)

Facility Managers and VPs in Commercial Real Estate and Construction

Industry/Entity Type

Real Estate

Requirements
Must have
• Commercial real estate oriented, relational wording, large catastrophic loss events
Should not have
• Sales and closing type words, no residential themes

```html
<!DOCTYPE html>
<html lang="en">
<head>
<meta charset="utf-8">
<title>Tallow Recovery — Large Loss Booklet Covers</title>
<link href="https://fonts.googleapis.com/css2?family=Open+Sans:wght@400;600;700&display=swap" rel="stylesheet">
<style>
  :root {
    --stage: #ecebe8;
    --paper: #f4f4f5;
    --amber: #d38f1c;
    --amber-deep: #b8770f;
    --navy: #1f3d7a;
    --badge: #e9d9b8;
    --wall-white: #f1f0ee;
    --wall-grey: #c9c4be;
    --floor-grey: #9e9890;
    --door-brown: #7a4a32;
    --sky-blue: #6fa8d8;
    --sky-cloud: #f2e6d6;
    --sun-glow: #fbe7b8;
    --tile-light: #e3a48a;
    --tile-deep: #b9654b;
    --batten: #efe3d6;
  }
  * { box-sizing: border-box; margin: 0; padding: 0; }
  html, body { width: 1200px; height: 800px; overflow: hidden; }
  body {
    background: var(--stage);
    font-family: "Open Sans", Arial, sans-serif;
    display: flex; align-items: center; justify-content: center;
  }
  .spread {
    display: flex; width: 1080px; height: 440px;
    box-shadow: 0 6px 24px rgba(0,0,0,.12);
  }
  .page {
    position: relative; width: 540px; height: 440px;
    background: var(--paper); overflow: hidden;
  }

  /* Back cover */
  .back-cover .interior-photo {
    position: absolute; inset: 0 0 118px 0;
    background:
      radial-gradient(ellipse 30% 45% at 42% 45%, rgba(255,255,255,.9), rgba(255,255,255,0) 70%),
      radial-gradient(ellipse 22% 60% at 8% 40%, rgba(122,74,50,.55), rgba(122,74,50,0) 70%),
      radial-gradient(ellipse 18% 55% at 82% 60%, rgba(122,74,50,.35), rgba(122,74,50,0) 70%),
      linear-gradient(180deg, var(--wall-white) 0%, var(--wall-grey) 62%, var(--floor-grey) 100%);
  }
  .back-cover .contact-band {
    position: absolute; left: 0; right: 0; bottom: 0; height: 118px;
    background: var(--amber);
    display: flex; align-items: center; justify-content: space-between;
    padding: 0 26px;
  }
  .contact-lines { color: #fff; font-size: 11px; line-height: 1.6; font-style: normal; }
  .contact-lines .divider { margin: 0 6px; }
  .affiliations { display: flex; gap: 8px; align-items: center; align-self: flex-end; margin-bottom: 22px; }
  .affiliation-badge { width: 30px; height: 22px; background: var(--badge); border-radius: 2px; }
  .affiliation-badge.round { width: 22px; border-radius: 50%; }

  /* Front cover */
  .front-cover .roof-photo {
    position: absolute; left: 0; right: 0; top: 0; height: 320px;
    background:
      radial-gradient(ellipse 40% 30% at 72% 38%, rgba(111,168,216,.85), rgba(111,168,216,0) 70%),
      radial-gradient(ellipse 45% 40% at 80% 75%, var(--sun-glow), rgba(251,231,184,0) 70%),
      radial-gradient(ellipse 35% 60% at 58% 85%, rgba(201,110,82,.9), rgba(201,110,82,0) 75%),
      radial-gradient(ellipse 25% 55% at 18% 55%, rgba(185,101,75,.8), rgba(185,101,75,0) 75%),
      linear-gradient(100deg, var(--batten) 0%, var(--tile-light) 35%, var(--sky-cloud) 70%, #cfdbe8 100%);
  }
  .front-cover .title-band {
    position: absolute; left: 0; right: 0; bottom: 0; height: 120px;
    padding: 0 30px;
  }
  .tagline {
    position: absolute; left: 30px; top: 22px;
    color: var(--amber); font-size: 16px; font-weight: 400; line-height: 1.3;
  }
  .brand {
    position: absolute; right: 30px; bottom: 24px;
    display: flex; align-items: center; gap: 10px;
    color: var(--amber-deep); font-size: 26px; font-weight: 700;
  }
  .brand-dot { width: 18px; height: 18px; border-radius: 50%; background: var(--navy); }
</style>
</head>
<body>
  <div class="spread">
    <section class="page back-cover">
      <div class="interior-photo" role="img" aria-label="Photo: gutted commercial interior during restoration, bare white walls, opened doorways, cables and debris on the floor"></div>
      <div class="contact-band">
        <address class="contact-lines">
          48 Harbor Point Dr Ste 210, Millbrook, Texas 75011<br>
          +1 800-555-0142<span class="divider">|</span>www.tallowrecovery.com
        </address>
        <div class="affiliations" aria-label="Industry affiliations">
          <span class="affiliation-badge"></span>
          <span class="affiliation-badge"></span>
          <span class="affiliation-badge"></span>
          <span class="affiliation-badge round"></span>
        </div>
      </div>
    </section>
    <section class="page front-cover">
      <div class="roof-photo" role="img" aria-label="Photo: roofer laying stacks of terracotta clay tiles on a large roof, blue sky and sunlit clouds behind"></div>
      <div class="title-band">
        <p class="tagline">Exceeding your expectations<br>when you need it most.</p>
        <div class="brand"><span class="brand-dot"></span>Tallow Recovery</div>
      </div>
    </section>
  </div>
</body>
</html>
```